EdTech startup needs web (& logo?) redesign

LectureLoop.com is a collection of fun online tools designed to help instructors in higher education (i.e. university) build a sense of community in the classroom and enable "active learning." We have spent most of our energy on developing functionality and would love to have some real designers contribute their ideas. Everything (logos, color scheme, images, etc.) is up for grabs, but the winning design should be bootstrap friendly. We are currently using the "Broadsheet" template, but are open to others. That being said, we are less interested in getting great code than a great design. Websites we admire include quizmarbleway.com, tradenest.com, and http://layouts.fetchtrellis.com/products/application

Pages we are particularly interested in ideas for include: homepage, lucky pick, the hook, and extra tambourine. The latter three currently use images that probably can't go mainstream.

If you want to participate in the contest we would love for you to check out the site first. In order to enable this, we have set up a fictional class (PLWQ 317-4 - Beta Website Redesign). Once you create an account at www.lectureloop.com, you just enter the super-secret invite code "k9trm27x" to add yourself to the class.

Attached our some files that were used to inspire our current design. Feel free to use or ignore them as you see fit. Thanks!

Target Market(s)

college students and their instructors

Industry/Entity Type

Education

Coding

Coded - Design and coding required

Number of Pages Required

4 page

Colors
0355a3
33a6d7
cee9f5

Requirements
Must have
• cool, fun design that is boostrap friendly.
Nice to have
• I like blue, but an open to other color themes.
Should not have
• ?

```html
<!DOCTYPE html>
<html lang="en">
<head>
<meta charset="utf-8">
<title>Welcome to LectureLoop!</title>
<link href="https://fonts.googleapis.com/css2?family=Arimo:wght@400;700&display=swap" rel="stylesheet">
<style>
  :root {
    --ink: #222;
    --ink-soft: #333;
    --paper: #ffffff;
    --band: #e9e9e9;
    --button: #3d8fd8;
    --button-edge: #2f7cc2;
    --link-border: #bbb;
    --icon: #222;
    --mascot-a: #d9d9d9;
    --mascot-b: #9a9a9a;
  }
  * { box-sizing: border-box; margin: 0; padding: 0; }
  html, body { width: 1200px; height: 872px; overflow: hidden; background: var(--paper); }
  body { font-family: "Arimo", Arial, sans-serif; color: var(--ink); position: relative; }

  .hero { position: absolute; left: 0; top: 0; width: 1200px; height: 330px; }
  .hero__mascot {
    position: absolute; left: 55px; top: 0; width: 365px; height: 330px;
    background: radial-gradient(ellipse at 50% 45%, var(--mascot-a), var(--mascot-b));
    border-radius: 0 0 46% 46%;
  }
  .hero__title {
    position: absolute; left: 484px; top: 34px;
    font-size: 50px; font-weight: 400; letter-spacing: -0.5px; color: var(--ink);
  }
  .hero__lede {
    position: absolute; left: 510px; top: 98px; width: 680px;
    font-size: 19px; line-height: 25px; color: var(--ink-soft);
  }
  .hero__signup {
    position: absolute; left: 660px; top: 183px; width: 292px; height: 52px;
    background: var(--button); border: 1px solid var(--button-edge); border-radius: 9px;
    color: #fff; font-size: 19px; line-height: 50px; text-align: center;
  }

  .tools {
    position: absolute; left: 0; top: 330px; width: 1200px; height: 542px;
    background: var(--band);
  }
  .tool { position: absolute; width: 278px; }
  .tool__name {
    display: flex; align-items: center; gap: 12px;
    font-size: 31px; font-weight: 400; color: var(--ink); height: 40px;
  }
  .tool__name svg { width: 28px; height: 28px; flex: none; }
  .tool__text {
    margin-top: 10px; font-size: 14px; line-height: 18px; font-weight: 700;
    color: var(--ink-soft); letter-spacing: -0.2px;
  }
  .tool__more {
    position: absolute; left: 0; width: 88px; height: 22px;
    border: 1px solid var(--link-border); background: var(--paper); border-radius: 3px;
    font-size: 12px; line-height: 20px; text-align: center; color: var(--ink);
  }
  .row-1 { top: 20px; }
  .row-2 { top: 293px; }
  .row-1 .tool__more { top: 209px; }
  .row-2 .tool__more { top: 213px; }
  .col-1 { left: 26px; } .col-2 { left: 319px; } .col-3 { left: 612px; } .col-4 { left: 902px; }
</style>
</head>
<body>
  <header class="hero">
    <div class="hero__mascot" role="img" aria-label="Mascot illustration: an owl wearing headphones"></div>
    <h1 class="hero__title">Welcome to LectureLoop!</h1>
    <p class="hero__lede">A collection of some fun and easy-to-use tools for building a classroom community and enabling active learning.</p>
    <div class="hero__signup">Sign up for an account &gt;</div>
  </header>

  <section class="tools">
    <article class="tool row-1 col-1">
      <h2 class="tool__name">Lucky Pick
        <svg viewBox="0 0 28 28"><path d="M4 17 A10 10 0 0 1 24 17" fill="none" stroke="var(--icon)" stroke-width="3"/><rect x="2" y="15" width="6" height="10" rx="2" fill="var(--icon)"/><rect x="20" y="15" width="6" height="10" rx="2" fill="var(--icon)"/></svg>
      </h2>
      <p class="tool__text">Where it all started! Students create playlists of upbeat music with VidStream. At the start of class, one lucky student gets to be the class DJ. Typically paired with a "fun fact" or "two truths and a lie" clicker activity.</p>
      <div class="tool__more">learn more &gt;</div>
    </article>

    <article class="tool row-1 col-2">
      <h2 class="tool__name">Flashcards
        <svg viewBox="0 0 28 28"><rect x="5" y="2" width="18" height="24" rx="2" fill="var(--icon)"/><path d="M16 5 L10 15 H14 L12 23 L19 12 H15 Z" fill="#fff"/></svg>
      </h2>
      <p class="tool__text">Get to know each other! With Flashcards you can "flip" through student (and instructor) profiles, learn names, and a little bit about what makes them tick. A great first step for creating an interactive classroom community.</p>
      <div class="tool__more">learn more &gt;</div>
    </article>

    <article class="tool row-1 col-3">
      <h2 class="tool__name">"The Hook"
        <svg viewBox="0 0 28 28"><path d="M14 2 V12 M14 12 L5 24 M14 12 L23 24 M14 12 V25" fill="none" stroke="var(--icon)" stroke-width="2.2" stroke-linecap="round"/></svg>
      </h2>
      <p class="tool__text">The hook chooses who will go and who will stay... well it randomly chooses a student from the class roster anyway. It's a fun way to encourage participation among quieter students and motivate active learning exercises.</p>
      <div class="tool__more">learn more &gt;</div>
    </article>

    <article class="tool row-1 col-4">
      <h2 class="tool__name">Virtual Clicker
        <svg viewBox="0 0 28 28"><rect x="9" y="2" width="10" height="24" fill="var(--icon)"/><path d="M9 7 H19 M9 12 H19 M9 17 H19 M9 22 H19" stroke="#fff" stroke-width="1.5"/></svg>
      </h2>
      <p class="tool__text">(coming soon) A simple tool for in-class polling. Launch multiple-choice questions from lectureloop.com or slides. Students respond via their laptop or smartphone. Bar graphs of the results (with "hook" capabilities) link to student profiles.</p>
      <div class="tool__more">learn more &gt;</div>
    </article>

    <article class="tool row-2 col-1">
      <h2 class="tool__name">Extra Tambourine
        <svg viewBox="0 0 28 28"><circle cx="14" cy="14" r="10" fill="none" stroke="var(--icon)" stroke-width="4"/><circle cx="14" cy="4" r="2.5" fill="var(--icon)"/><circle cx="14" cy="24" r="2.5" fill="var(--icon)"/></svg>
      </h2>
      <p class="tool__text">Sometimes the think-pair-share discussions get so feverish the only prescription is more rhythm! In other words, when the class gets too noisy you can ring this virtual bell to get everyone's attention.</p>
      <div class="tool__more">learn more &gt;</div>
    </article>

    <article class="tool row-2 col-2">
      <h2 class="tool__name">Student Profiles
        <svg viewBox="0 0 28 28"><circle cx="14" cy="8" r="6" fill="var(--icon)"/><path d="M3 27 C3 18 25 18 25 27 Z" fill="var(--icon)"/></svg>
      </h2>
      <p class="tool__text">Instructor-customizable profiles let students share information about themselves with the class. Use it to find out what students expect to learn, their previous course-work, or just to help people get to know each other (see flashcards).</p>
      <div class="tool__more">learn more &gt;</div>
    </article>

    <article class="tool row-2 col-3">
      <h2 class="tool__name">Self/Peer Evals
        <svg viewBox="0 0 28 28"><rect x="3" y="5" width="20" height="20" fill="none" stroke="var(--icon)" stroke-width="3"/><path d="M8 14 L13 19 L25 4" fill="none" stroke="var(--icon)" stroke-width="3.5"/></svg>
      </h2>
      <p class="tool__text">(coming Spring 2016) Self/Peer evaluations are a fantastic way to help students master material and deliver high quality feedback - fast. Works great in both large and small classes to reflect on group assignments or exams.</p>
      <div class="tool__more">learn more &gt;</div>
    </article>

    <article class="tool row-2 col-4">
      <h2 class="tool__name">Rubrics
        <svg viewBox="0 0 28 28"><rect x="2" y="2" width="24" height="24" fill="var(--icon)"/><path d="M2 8 H26 M2 14 H26 M2 20 H26 M8 2 V26 M14 2 V26 M20 2 V26" stroke="#fff" stroke-width="1.3"/></svg>
      </h2>
      <p class="tool__text">(coming Spring 2016) Rubrics are a great tool - both for providing guidance and feedback. This tool lets you create your own rubrics to use for assignments (or peer evals for example). Also, you can search a database of existing rubrics to use as a starting point.</p>
      <div class="tool__more">learn more &gt;</div>
    </article>
  </section>
</body>
</html>
```